Northern Summit Builders & Affiliates Redesigning our Look

We need stationary (letterhead, envelopes, notepads, invoicing templates, etc) that all coordinate. We are an commerial and residential exteriors construction company that operates 3 companies which all run exclusively, however, the compliment one another well.

Northern Summit Builders (this company installs exteriors on jobsites both residential and commercial)
Northern Summit Roofing & Building Supply (this company sells exterior building materials to homeowners and builders.)
Northern Summit Dumpster Services (This company delivers roll away dumpster cans to homeowners and builders)

Just a note: When I say we do exterior work. We do roofing, siding, stone, windows/doors, gutters, and decks.

We are looking for stationary that includes all three and keeps with our patriotic theme

Info on our firm:
Address: 2718 Tamarind Rd, Elkton MI 48512
Phone: 231-555-0172
Website: www.northernsummit-example.us

Target Market(s)

Our companies target market is vast. We work in the B2B space as well as with homeowner (retail customers). We are in the home and commercial buiding construction field. We specialized in exteriors. (Roofing, Siding, Stone, Windows, Doors, Decks, Gutters)

Industry/Entity Type

Construction

Colors
ec1f27
ffffff
0555a3

Requirements
Must have
• Would like to have a clean professional look with a patriotic theme
Nice to have
• Red/White/Blue

```html
<!DOCTYPE html>
<html lang="en">
<head>
<meta charset="utf-8">
<title>Northern Summit Roofing &amp; Building Supply – Letterhead</title>
<link rel="stylesheet" href="https://fonts.googleapis.com/css2?family=Source+Sans+3:wght@400;600&display=swap">
<style>
  :root {
    --backdrop: #e8e8ea;
    --paper: #ffffff;
    --brand-red: #e1262b;
    --brand-navy: #18194f;
    --ink: #18194f;
    --on-red: #ffffff;
  }
  html, body {
    margin: 0;
    width: 1200px;
    height: 1062px;
    overflow: hidden;
    background: var(--backdrop);
    font-family: "Source Sans 3", "Helvetica Neue", Arial, sans-serif;
  }
  .letterhead {
    position: absolute;
    left: 213px;
    top: 31px;
    width: 773px;
    height: 1000px;
    background: var(--paper);
    box-shadow: 0 2px 10px rgba(0,0,0,0.12);
    overflow: hidden;
  }
  .brand {
    position: absolute;
    left: 62px;
    top: 70px;
    display: flex;
    align-items: center;
    gap: 12px;
  }
  .brand-mark {
    width: 18px;
    height: 18px;
    background: var(--brand-red);
    flex: none;
  }
  .brand-name {
    font-size: 22px;
    font-weight: 600;
    line-height: 1.15;
    color: var(--ink);
    max-width: 240px;
  }
  .footer-wave {
    position: absolute;
    left: 0;
    top: 0;
    width: 773px;
    height: 1000px;
  }
  .wave-navy { fill: var(--brand-navy); }
  .wave-red { fill: var(--brand-red); }
  .contact {
    position: absolute;
    right: 38px;
    bottom: 42px;
    color: var(--on-red);
    font-size: 13px;
    line-height: 1.6;
    text-align: right;
  }
  .contact-line {
    display: flex;
    justify-content: flex-end;
    align-items: center;
    gap: 8px;
  }
  .contact-item {
    display: inline-flex;
    align-items: center;
    gap: 4px;
  }
  .contact-icon {
    width: 11px;
    height: 11px;
    fill: none;
    stroke: var(--on-red);
    stroke-width: 1.6;
  }
</style>
</head>
<body>
  <main class="letterhead">
    <header class="brand">
      <span class="brand-mark"></span>
      <span class="brand-name">Northern Summit Roofing &amp; Building Supply</span>
    </header>

    <svg class="footer-wave" viewBox="0 0 773 1000" aria-hidden="true">
      <path class="wave-navy" d="M0,905 C250,915 380,800 520,770 C620,748 700,745 773,742 L773,1000 L0,1000 Z"/>
      <path class="wave-red" d="M0,919 C250,929 390,815 525,786 C620,765 700,760 773,758 L773,1000 L0,1000 Z"/>
    </svg>

    <footer class="contact">
      <div class="contact-line">2718 Tamarind Rd, Elkton MI 48512</div>
      <div class="contact-line">
        <span class="contact-item">
          <svg class="contact-icon" viewBox="0 0 12 12"><path d="M2,1 L4.5,1 L5.5,3.5 L4,4.5 C4.8,6.2 5.8,7.2 7.5,8 L8.5,6.5 L11,7.5 L11,10 C6,10.5 1.5,6 2,1 Z"/></svg>
          231-555-0172
        </span>
        <span class="contact-item">
          <svg class="contact-icon" viewBox="0 0 12 12"><rect x="1" y="2.5" width="10" height="7"/><path d="M1,2.5 L6,6.5 L11,2.5"/></svg>
          info@northernsummit-example.us
        </span>
        <span class="contact-item">
          <svg class="contact-icon" viewBox="0 0 12 12"><circle cx="6" cy="6" r="5"/><path d="M1,6 H11 M6,1 C3.5,4 3.5,8 6,11 M6,1 C8.5,4 8.5,8 6,11"/></svg>
          www.northernsummit-example.us
        </span>
      </div>
    </footer>
  </main>
</body>
</html>
```